Law Office Business Card

We need a business card design to include the following information:
Name of Firm: Brennick Law Group, P.A.
Address: 4627 Sandlot Ave, Ste 208, Coral Mesa, FL 33990
Phone: 561-555-0148
Fax: 561-555-0193
Website: http://www.tbrennicklaw.example

We Need a place for the Person's name and email address. Please start with the following:
Lorna K. Dwyer, Esq.
lorna@tbrennicklaw.example

```html
<!DOCTYPE html>
<html lang="en">
<head>
<meta charset="utf-8">
<title>Brennick Law Group, P.A. — Business Card</title>
<link href="https://fonts.googleapis.com/css2?family=Tinos:wght@400;700&display=swap" rel="stylesheet">
<style>
  :root {
    --backdrop: #ecebe8;
    --card-white: #ffffff;
    --band-blue: #135573;
    --ink-grey: #6f6f6f;
    --mark-grey: #8a8a8a;
    --on-blue: #ffffff;
  }
  * { margin: 0; padding: 0; box-sizing: border-box; }
  html, body {
    width: 1200px;
    height: 768px;
    overflow: hidden;
    background: var(--backdrop);
    font-family: "Tinos", "Times New Roman", serif;
  }
  .card {
    position: absolute;
    left: 80px;
    top: 82px;
    width: 1040px;
    height: 604px;
    background: var(--card-white);
    overflow: hidden;
    box-shadow: 0 2px 6px rgba(0,0,0,0.12);
  }
  .card__band {
    position: absolute;
    left: 0;
    top: 262px;
    width: 100%;
    height: 342px;
    background: var(--band-blue);
  }
  .brand-box {
    position: absolute;
    left: 62px;
    top: 65px;
    width: 352px;
    height: 289px;
    background: var(--card-white);
    box-shadow: 0 3px 10px rgba(0,0,0,0.35);
    display: flex;
    flex-direction: column;
    align-items: center;
    justify-content: center;
    gap: 14px;
  }
  .brand-box__square {
    width: 46px;
    height: 46px;
    border: 3px solid var(--mark-grey);
  }
  .brand-box__name {
    color: var(--mark-grey);
    font-weight: 400;
    font-size: 38px;
    line-height: 1.15;
    text-align: center;
  }
  .person-name {
    position: absolute;
    left: 453px;
    top: 206px;
    color: var(--ink-grey);
    font-weight: 700;
    font-size: 35px;
    line-height: 1;
  }
  .contact-list {
    position: absolute;
    left: 453px;
    top: 276px;
    list-style: none;
    color: var(--on-blue);
    font-size: 28px;
  }
  .contact-list li {
    display: flex;
    align-items: center;
    height: 46px;
  }
  .contact-list svg {
    width: 28px;
    height: 28px;
    margin-right: 18px;
    flex: none;
  }
  .address {
    position: absolute;
    left: 125px;
    top: 516px;
    display: flex;
    align-items: center;
    color: var(--on-blue);
    font-size: 29px;
  }
  .address svg {
    width: 26px;
    height: 38px;
    margin-right: 10px;
  }
</style>
</head>
<body>
  <div class="card">
    <div class="card__band"></div>

    <div class="brand-box">
      <div class="brand-box__square"></div>
      <div class="brand-box__name">Brennick<br>Law Group, P.A.</div>
    </div>

    <div class="person-name">Lorna K. Dwyer, Esq.</div>

    <ul class="contact-list">
      <li>
        <svg viewBox="0 0 28 28" aria-hidden="true"><rect x="3" y="7" width="22" height="15" fill="none" stroke="#fff" stroke-width="2"/><path d="M3 7 L14 16 L25 7" fill="none" stroke="#fff" stroke-width="2"/></svg>
        lorna@tbrennicklaw.example
      </li>
      <li>
        <svg viewBox="0 0 28 28" aria-hidden="true"><path d="M8 3 L12 8 L10 11 C11 14 14 17 17 18 L20 16 L25 20 L22 25 C13 24 4 15 3 6 Z" fill="#fff"/></svg>
        561-555-0148
      </li>
      <li>
        <svg viewBox="0 0 28 28" aria-hidden="true"><rect x="8" y="3" width="12" height="8" fill="none" stroke="#fff" stroke-width="2"/><rect x="3" y="11" width="22" height="10" rx="1" fill="#fff"/><rect x="8" y="19" width="12" height="6" fill="#fff" stroke="#135573" stroke-width="1"/></svg>
        561-555-0193
      </li>
      <li>
        <svg viewBox="0 0 28 28" aria-hidden="true"><circle cx="14" cy="14" r="11" fill="none" stroke="#fff" stroke-width="2"/><ellipse cx="14" cy="14" rx="5" ry="11" fill="none" stroke="#fff" stroke-width="1.6"/><line x1="3" y1="14" x2="25" y2="14" stroke="#fff" stroke-width="1.6"/><line x1="14" y1="3" x2="14" y2="25" stroke="#fff" stroke-width="1.6"/></svg>
        www.tbrennicklaw.example
      </li>
    </ul>

    <div class="address">
      <svg viewBox="0 0 26 38" aria-hidden="true"><path d="M13 1 C6 1 1 6 1 13 C1 22 13 37 13 37 C13 37 25 22 25 13 C25 6 20 1 13 1 Z" fill="#fff"/><circle cx="13" cy="13" r="4.5" fill="#135573"/></svg>
      4627 Sandlot Ave, Ste 208, Coral Mesa, FL&nbsp; 33990
    </div>
  </div>
</body>
</html>
```